New Packaging Design Project

Wine packaging redesign. Retail partner requested a redesign of a private label wine. The old label is attached. Our partner liked the Lantern and Briar label and wanted something similar. There will be a logo added to the top of the label

Went on vacation/holiday

```html
<!DOCTYPE html>
<html lang="en">
<head>
<meta charset="utf-8">
<title>Napa Valley Red Blend – Label</title>
<link rel="stylesheet" href="https://fonts.googleapis.com/css2?family=Marcellus&family=Fira+Sans+Condensed:wght@400;500&display=swap">
<style>
  :root {
    --backdrop-top: #d9d9d9;
    --backdrop-bottom: #f4f4f4;
    --label-black: #111112;
    --gold: #c49a4a;
    --gold-soft: #a8823f;
    --ink-light: #e6e6e6;
    --hill-dark: #2b2b2d;
    --hill-mid: #4a4a4c;
    --hill-gold: #9c7a3c;
  }
  * { margin: 0; padding: 0; box-sizing: border-box; }
  html, body {
    width: 1200px;
    height: 1200px;
    overflow: hidden;
  }
  body {
    background: linear-gradient(180deg, var(--backdrop-top), var(--backdrop-bottom));
    position: relative;
  }
  .wine-label {
    position: absolute;
    left: 300px;
    top: 100px;
    width: 600px;
    height: 1000px;
    background: var(--label-black);
    overflow: hidden;
  }
  .label-heading {
    position: absolute;
    top: 190px;
    width: 100%;
    text-align: center;
  }
  .region-name {
    font-family: "Marcellus", serif;
    font-weight: 400;
    font-size: 58px;
    letter-spacing: 1px;
    color: var(--gold);
    line-height: 1;
  }
  .wine-style {
    margin-top: 42px;
    font-family: "Fira Sans Condensed", sans-serif;
    font-weight: 400;
    font-size: 36px;
    letter-spacing: 1px;
    color: var(--ink-light);
    line-height: 1;
  }
  .vintage-row {
    margin-top: 12px;
    display: flex;
    align-items: center;
    justify-content: center;
    gap: 16px;
  }
  .vintage-rule {
    width: 100px;
    height: 1px;
    background: var(--gold-soft);
  }
  .vintage {
    font-family: "Fira Sans Condensed", sans-serif;
    font-size: 22px;
    color: var(--gold);
    line-height: 1;
  }
  .varietals {
    margin-top: 22px;
    font-family: "Fira Sans Condensed", sans-serif;
    font-weight: 400;
    font-size: 21px;
    letter-spacing: 0.5px;
    color: var(--ink-light);
    line-height: 1.4;
  }
  .landscape-art {
    position: absolute;
    left: 0;
    top: 480px;
    width: 100%;
    height: 520px;
    background: linear-gradient(180deg,
      var(--label-black) 0%,
      var(--hill-dark) 20%,
      var(--hill-mid) 45%,
      var(--hill-gold) 72%,
      var(--hill-dark) 100%);
  }
</style>
</head>
<body>
  <main class="wine-label">
    <header class="label-heading">
      <h1 class="region-name">NAPA VALLEY</h1>
      <p class="wine-style">RED BLEND</p>
      <div class="vintage-row">
        <span class="vintage-rule"></span>
        <span class="vintage">2018</span>
        <span class="vintage-rule"></span>
      </div>
      <p class="varietals">MERLOT | CABERNET SAUVIGNON<br>CABERNET FRANC | PETIT VERDOT | MALBEC</p>
    </header>
    <div class="landscape-art" role="img" aria-label="Illustration of grey layered mountains over rolling gold vineyard rows"></div>
  </main>
</body>
</html>
```